Stationary for Beauty and Spa School

Create a business card, letterhead and envelopes (primarily #10 envelope with and without window and catalog envelope) for a beauty and wellness school in Miami, Fl. We offer 8 different programs of study and need an eye catching look. Looking for a combination of modern yet sophisticated. Nothing corporate or business looking. Would like to have a look and feel that is similar (or incorporates aspects) of a new website we will be launching in the next 30 days (screen shot attached.)

The final design should communicate style and elegance in a down to earth and friendly way. We strive to provide our students with quality education, friendly and amicable staff and experienced instructors.
Updates

Hello. FYI, in order to print an aesthetically appealing business card, we would like to print them (the business cards) using silk printing method, with spot UV coating (on some elements, maybe the logo, or depending on the design) and die cuts. Please think of this when preparing your design.

Only 1 day left, please submit your designs for selection. Thanks

Target Market(s)

Adults 18-49 years who are mostly interested in beauty and fashion. Need a youthful & modern look, yet sophisticated and elegant.

Industry/Entity Type

School

Colors
e34197
6b449b
add136
f79021

Requirements
Must have
• Similar look and feel as website (see attached screen shot)
Same look and feel of website (see attached screenshot)
Logo
Address: 5216 SW 3rd Avenue. Miami, Fl 33155
Telephone: 305-514-9382
Fax: 786-420-5163
website/url: www.luminora.edu
incorporate Photo of blonde model (attached)
Nice to have
• Tag line: "Beautify your future." Also, maybe two-sided business card. Would be nice if we could mention our programs (maybe in the back of the card). Below are the program offerings (names cannot be changed but order is irrelevant)... Cosmetology, Barber, Spa Therapy, Massage Therapy, Makeup Artistry, Skin Care, Manicure, Pedicure & Nail Extensions, Full Specialist.

A design with text plus a beautiful photo of a model is appealing. Attached to the files is a sample of a cover for a student handbook we have created. You should use the photo of the blonde model (attached) in your design. The original (quality) version of this stock photograph has been uploaded.

Also would be nice to request clients to follow us on facebook and instagram by including the icons.
Should not have
• A corporate or business look. We are a vocational school teaching beauty and spa programs and we like our advertising to have a look that resembles the industry. We do not want a very serious look or snobby feel.

```html
<!DOCTYPE html>
<html lang="en">
<head>
<meta charset="utf-8">
<title>Luminora School of Beauty – Card</title>
<link rel="stylesheet" href="https://fonts.googleapis.com/css2?family=Jost:wght@300;400;500;600&display=swap">
<style>
  :root {
    --ink: #111111;
    --paper: #ffffff;
    --violet: #5a12f0;
    --orchid: #c03ef0;
    --amber: #f0aa1e;
    --teal: #2bb59a;
    --lime: #a4e02a;
  }
  * { box-sizing: border-box; margin: 0; padding: 0; }
  html, body { width: 1050px; height: 1200px; overflow: hidden; background: var(--paper); }
  .card {
    position: relative;
    width: 1050px;
    height: 1200px;
    background: var(--paper);
    font-family: "Jost", sans-serif;
    color: var(--ink);
  }
  .rule {
    position: absolute;
    left: 0;
    width: 1050px;
    background: var(--ink);
  }
  .rule--top { top: 0; height: 4px; }
  .rule--mid { top: 607px; height: 4px; }

  .brand {
    position: absolute;
    top: 215px;
    left: 0;
    width: 1050px;
    text-align: center;
    color: var(--ink);
    font-weight: 500;
  }
  .brand__name {
    display: block;
    font-size: 150px;
    line-height: 1;
    letter-spacing: 2px;
  }
  .brand__sub {
    display: block;
    margin-top: 14px;
    font-size: 38px;
    letter-spacing: 1px;
    text-transform: uppercase;
  }

  .tagline {
    position: absolute;
    top: 694px;
    left: 0;
    width: 1050px;
    text-align: center;
    font-size: 54px;
    font-weight: 400;
    letter-spacing: 21px;
    padding-left: 21px;
    text-transform: uppercase;
    line-height: 1;
  }

  .programs {
    position: absolute;
    top: 818px;
    right: 538px;
    text-align: right;
    font-size: 36px;
    line-height: 45px;
    font-weight: 300;
    white-space: nowrap;
  }
  .programs .accent { font-weight: 500; }
  .programs .strong { font-weight: 500; color: var(--ink); }
  .c-orchid { color: var(--orchid); }
  .c-amber { color: var(--amber); }
  .c-teal { color: var(--teal); }
  .c-lime { color: var(--lime); }

  .divider {
    position: absolute;
    left: 563px;
    top: 822px;
    width: 2px;
    height: 220px;
    background: var(--ink);
  }

  .contact {
    position: absolute;
    left: 610px;
    top: 822px;
    list-style: none;
    font-size: 24px;
    line-height: 30px;
    font-weight: 300;
  }
  .contact__item {
    display: flex;
    align-items: flex-start;
  }
  .contact__item + .contact__item { margin-top: 30px; }
  .contact__icon {
    width: 54px;
    height: 54px;
    flex: 0 0 54px;
    margin-right: 10px;
  }
  .contact__item--web { margin-top: 22px !important; align-items: center; }
  .contact__item--web .contact__icon { width: 54px; height: 46px; }

  .follow {
    position: absolute;
    top: 1097px;
    left: 346px;
    display: flex;
    align-items: center;
  }
  .follow__dot {
    width: 48px;
    height: 48px;
    border-radius: 50%;
    background: var(--violet);
    margin-right: 7px;
  }
  .follow__label {
    margin-left: 16px;
    font-size: 29px;
    font-weight: 400;
    letter-spacing: 6px;
    text-transform: uppercase;
  }
</style>
</head>
<body>
<main class="card">
  <div class="rule rule--top"></div>

  <h1 class="brand">
    <span class="brand__name">Luminora</span>
    <span class="brand__sub">School of Beauty</span>
  </h1>

  <div class="rule rule--mid"></div>

  <p class="tagline">Beautify your future</p>

  <p class="programs">
    <span class="accent c-orchid">cosmetology</span> barber <span class="accent c-amber">spa</span><br>
    <span class="accent c-amber">therapy</span> <span class="strong">massage therapy</span><br>
    makeup artistry <span class="accent c-teal">skin care</span><br>
    <span class="accent c-orchid">manicure</span> <span class="strong">pedicure</span> <span class="accent c-lime">nail</span><br>
    <span class="accent c-lime">extensions</span> full specialist
  </p>

  <div class="divider"></div>

  <ul class="contact">
    <li class="contact__item">
      <svg class="contact__icon" viewBox="0 0 54 54" aria-hidden="true">
        <path d="M26 4 C15 4 8 12 8 21 C8 32 26 52 26 52 C26 52 44 32 44 21 C44 12 37 4 26 4 Z" fill="#111"/>
        <circle cx="26" cy="20" r="6.5" fill="#fff"/>
      </svg>
      <span>5216 SW 3rd Avenue.<br>Miami, Fl 33155</span>
    </li>
    <li class="contact__item">
      <svg class="contact__icon" viewBox="0 0 54 54" aria-hidden="true">
        <path d="M2 14 C8 6 46 6 52 14 L52 20 L42 20 L40 14 L14 14 L12 20 L2 20 Z" fill="#111"/>
        <path d="M15 22 L39 22 L46 40 L8 40 Z" fill="#111"/>
        <circle cx="27" cy="30" r="5" fill="#fff"/>
        <circle cx="27" cy="30" r="2.5" fill="#111"/>
      </svg>
      <span>Telephone: 305-514-9382<br>Fax: 786-420-5163</span>
    </li>
    <li class="contact__item contact__item--web">
      <svg class="contact__icon" viewBox="0 0 54 46" aria-hidden="true">
        <g fill="none" stroke="#111" stroke-width="2">
          <circle cx="27" cy="23" r="21"/>
          <ellipse cx="27" cy="23" rx="9" ry="21"/>
          <line x1="27" y1="2" x2="27" y2="44"/>
          <line x1="6" y1="23" x2="48" y2="23"/>
          <path d="M10 12 H44 M10 34 H44"/>
        </g>
      </svg>
      <span>www.luminora.edu</span>
    </li>
  </ul>

  <div class="follow">
    <span class="follow__dot" aria-hidden="true"></span>
    <span class="follow__dot" aria-hidden="true"></span>
    <span class="follow__label">Follow us!</span>
  </div>
</main>
</body>
</html>
```